Business Card Design

Lawn service

Industry/Entity Type

Business

Contact Information for Business Card

Fernway Turf & Garden , marla dunwick/owner,operater,2146 hollister creekrd.. w. statesboro,ga. 30458, phone:555-274-0963, Residential,Commercial, Lawn and Landscape Maintenance, Bushhogging

```html
<!DOCTYPE html>
<html lang="en">
<head>
<meta charset="utf-8">
<title>Fernway Turf &amp; Garden – Business Card</title>
<link rel="stylesheet" href="https://fonts.googleapis.com/css2?family=Bitter:wght@700&family=Open+Sans:wght@400;600;700&display=swap">
<style>
  :root {
    --page-bg: #e9e6e1;
    --card-bg: #fbfbfa;
    --brand-green: #2f8a2a;
    --deep-green: #1f6b1e;
    --text-grey: #9a9a9a;
    --label-grey: #a7a7a7;
    --band-text: #ffffff;
  }
  * { margin: 0; padding: 0; box-sizing: border-box; }
  html, body {
    width: 1200px;
    height: 805px;
    overflow: hidden;
    background: var(--page-bg);
  }
  .stage {
    width: 1200px;
    height: 805px;
    display: flex;
    align-items: center;
    justify-content: center;
  }
  .business-card {
    position: relative;
    width: 1000px;
    height: 572px;
    background: var(--card-bg);
    box-shadow: 0 10px 30px rgba(0,0,0,0.18);
    overflow: hidden;
  }
  .brand {
    position: absolute;
    left: 52px;
    top: 74px;
    display: flex;
    align-items: center;
    gap: 16px;
  }
  .brand-dot {
    width: 24px;
    height: 24px;
    border-radius: 50%;
    background: var(--brand-green);
    flex-shrink: 0;
  }
  .brand-name {
    font-family: "Bitter", Georgia, serif;
    font-weight: 700;
    font-size: 44px;
    line-height: 1.1;
    color: var(--brand-green);
    letter-spacing: 0.5px;
    white-space: nowrap;
  }
  .contact {
    position: absolute;
    left: 62px;
    top: 218px;
  }
  .person-name {
    font-family: "Bitter", Georgia, serif;
    font-weight: 700;
    font-size: 36px;
    color: var(--brand-green);
    line-height: 1.1;
  }
  .person-role {
    font-family: "Open Sans", Arial, sans-serif;
    font-size: 15px;
    color: var(--label-grey);
    margin-top: 2px;
  }
  .address {
    font-family: "Open Sans", Arial, sans-serif;
    font-style: normal;
    font-size: 23px;
    color: var(--text-grey);
    line-height: 1.45;
    margin-top: 26px;
    letter-spacing: 0.4px;
  }
  .phone {
    display: flex;
    align-items: center;
    gap: 18px;
    margin-top: 36px;
  }
  .phone-icon { width: 30px; height: 30px; flex-shrink: 0; }
  .phone-number {
    font-family: "Open Sans", Arial, sans-serif;
    font-weight: 700;
    font-size: 30px;
    color: var(--deep-green);
    letter-spacing: 4px;
  }
  .services-band {
    position: absolute;
    left: 0;
    bottom: 0;
    width: 100%;
  }
  .services-list {
    height: 52px;
    background: var(--brand-green);
    display: flex;
    align-items: center;
    padding-left: 62px;
    font-family: "Open Sans", Arial, sans-serif;
    font-weight: 600;
    font-size: 19px;
    color: var(--band-text);
    letter-spacing: 0.6px;
    white-space: nowrap;
  }
  .services-list .sep { margin: 0 10px; }
  .services-edge {
    height: 20px;
    background: var(--deep-green);
  }
</style>
</head>
<body>
  <main class="stage">
    <article class="business-card">
      <header class="brand">
        <span class="brand-dot"></span>
        <h1 class="brand-name">Fernway Turf &amp; Garden</h1>
      </header>

      <section class="contact">
        <h2 class="person-name">Marla Dunwick</h2>
        <p class="person-role">Owner/Operater</p>
        <address class="address">
          2146 Hollister Creek Rd West<br>
          Cedar Hollow, GA 31099
        </address>
        <p class="phone">
          <svg class="phone-icon" viewBox="0 0 30 30" aria-hidden="true">
            <circle cx="15" cy="15" r="15" fill="var(--brand-green)"/>
            <path d="M10.5 8.2c.6-.5 1.4-.4 1.8.2l1.6 2.4c.4.6.3 1.3-.2 1.8l-.9.8c.9 1.8 2.2 3.1 4 4l.8-.9c.5-.5 1.2-.6 1.8-.2l2.4 1.6c.6.4.7 1.2.2 1.8l-1.1 1.3c-.6.7-1.6.9-2.5.6-4.2-1.5-7.3-4.6-8.8-8.8-.3-.9-.1-1.9.6-2.5z" fill="#fff"/>
          </svg>
          <span class="phone-number">555-274-0963</span>
        </p>
      </section>

      <footer class="services-band">
        <p class="services-list">
          Residential<span class="sep">•</span>Commercial<span class="sep">•</span>Lawn and Landscape Maintenance<span class="sep">•</span>Bushhogging
        </p>
        <div class="services-edge"></div>
      </footer>
    </article>
  </main>
</body>
</html>
```